Bluewater Getaways KT needs a new Website

We have an old website that is just that - old. We need a fresh website that is professional graphic designed that has the following features.
1. Can be updated by ourselves in some areas.
2. Has a shopping cart.
3. Has links to download PDF files
4. Has links to other pages in the website
5. Includes social media links
6. Has a client log-in area
Full details in brief provided.

SORRY BUT IT'S URGENT. We've taken too long to write the details and it is now urgent. So my apologies I will be asking for designers to work quickly.

We will continue to use our existing web hosting company and url. Their is a link to the old website in the Design Brief.
Updates

UPDATE:  Please see the new file UPDATE TO DESIGN BRIEF.
Thanks for all your submissions to date.  We hope the update will assist with your designs.
As indicated in previous messages, we are happy with the Home Page + 1 Page in order to select the designer to work with in creating the full design. 

Thankyou Designers.  Much appreciate your efforts.
It's getting late here on Norfolk so I won't have much chance too review any more designs this evening.
But for your information:
Designer 7318405 Ravindra Mehta is so far the closest to what we are seeking.
Thanks again. 

Reason: Have extended to Monday 7 October to give time for designers to submit after feedback today. Especially given the time differences

Target Market(s)

Very wide audience. Current client group not that tech savvy, but we hope to broaden our market and sell more creative products, and so website needs to consider how people now use media, ie tablets & iphones.

Industry/Entity Type

Shopping

Requirements
Nice to have
• PLEASE SEE THE "UPDATE TO THE DESIGN BRIEF"

```html
<!DOCTYPE html>
<html lang="en">
<head>
<meta charset="utf-8">
<title>Bluewater Getaways KT</title>
<link href="https://fonts.googleapis.com/css2?family=Mulish:wght@400;600;700;800&family=Kaushan+Script&display=swap" rel="stylesheet">
<style>
:root{
  --orange:#f58220;
  --green:#14a05a;
  --text:#555;
  --muted:#777;
  --band:#f4f4f4;
  --rule:#bbb;
}
*{margin:0;padding:0;box-sizing:border-box}
html,body{width:1200px;height:861px;overflow:hidden;background:#fff;font-family:"Mulish",sans-serif;color:var(--text)}
.page{position:relative;width:1200px;height:861px}
.nav{position:absolute;left:201px;top:18px;height:18px;width:797px;display:flex;align-items:center;font-size:11.5px;letter-spacing:.2px;text-transform:uppercase;white-space:nowrap}
.nav a{color:var(--green);text-decoration:none;display:flex;align-items:center;padding:0 15px;border-left:1px dotted #444;line-height:12px}
.nav a:first-child{padding-left:0;border-left:0;color:var(--orange)}
.nav .caret{display:inline-block;width:0;height:0;border-left:4px solid transparent;border-right:4px solid transparent;border-top:5px solid var(--orange);margin-left:5px}
.nav .social{margin-left:auto;display:flex;gap:6px;align-items:center;border-left:1px dotted #444;padding-left:40px;height:12px}
.nav .social span{width:9px;height:9px;border-radius:50%;background:var(--orange)}
.rule-top{position:absolute;left:200px;top:50px;width:799px;border-top:1px dotted var(--rule)}
.brand{position:absolute;left:201px;top:82px;display:flex;align-items:center;gap:12px}
.brand .dot{width:58px;height:58px;border-radius:50%;background:var(--orange)}
.brand .name{font-size:26px;font-weight:800;color:var(--orange);line-height:1.05;width:210px}
.search{position:absolute;left:702px;top:86px;display:flex}
.search input{width:223px;height:22px;border:1px solid #ddd;font:10px "Mulish",sans-serif;padding:0 6px;color:#999}
.search button{width:29px;height:22px;border:0;background:var(--orange);display:flex;align-items:center;justify-content:center}
.help{position:absolute;right:205px;top:116px;display:flex;align-items:baseline;gap:10px;white-space:nowrap;font-size:10px;color:#333;text-transform:uppercase}
.help strong{font-size:17px;font-weight:800;color:var(--green);letter-spacing:-.4px}
.hero{position:absolute;left:0;top:174px;width:1200px;height:360px;border-top:1px dotted #fff;background:linear-gradient(180deg,#7a8590 0%,#5f93b9 18%,#4a9ccd 45%,#6cb5dc 75%,#86c3e3 100%)}
.hero-shadow{position:absolute;left:180px;top:534px;width:840px;height:14px;background:radial-gradient(ellipse at top,rgba(0,0,0,.12),rgba(0,0,0,0) 70%)}
.tagline{position:absolute;left:0;top:550px;width:1200px;text-align:center;font-family:"Kaushan Script",cursive;font-weight:400;color:#a9a9a9;white-space:nowrap}
.tagline .big{font-size:48px}
.tagline .small{font-size:25px;margin-left:6px}
.footer{position:absolute;left:0;top:630px;width:1200px;height:231px;background:var(--band)}
.col{position:absolute;top:17px}
.col svg{display:block;height:38px}
.col h3{position:absolute;top:66px;left:0;white-space:nowrap;font-size:12px;font-weight:700;color:#444;text-transform:uppercase;letter-spacing:-.1px}
.col p{position:absolute;top:89px;left:0;white-space:nowrap;font-size:10.3px;line-height:15.6px;color:var(--muted)}
.col p.tight{line-height:14px}
.divider{position:absolute;top:70px;height:98px;border-left:1px dotted #aaa}
.rule-bottom{position:absolute;left:200px;top:189px;width:799px;border-top:1px dotted var(--rule)}
.copy{position:absolute;left:202px;top:204px;font-size:10.5px;color:#888}
</style>
</head>
<body>
<div class="page">
  <nav class="nav">
    <a href="#">Home</a>
    <a href="#">Overview<span class="caret"></span></a>
    <a href="#">Norfolk Island Services<span class="caret"></span></a>
    <a href="#">Our Shop<span class="caret"></span></a>
    <a href="#">Make a Booking<span class="caret"></span></a>
    <a href="#">Testimonials</a>
    <div class="social"><span></span><span></span></div>
  </nav>
  <div class="rule-top"></div>

  <div class="brand">
    <div class="dot"></div>
    <div class="name">Bluewater Getaways KT</div>
  </div>

  <form class="search">
    <input type="text" value="SEARCH HERE" aria-label="Search">
    <button type="button" aria-label="Search"><svg width="12" height="12" viewBox="0 0 12 12"><circle cx="5" cy="5" r="3.6" fill="none" stroke="#fff" stroke-width="1.6"/><line x1="7.6" y1="7.6" x2="11" y2="11" stroke="#fff" stroke-width="1.8"/></svg></button>
  </form>
  <div class="help">If need any help call us today <strong>+ 64 9 555 0182</strong></div>

  <div class="hero" role="img" aria-label="Photo of a kayaker paddling a yellow kayak in clear blue water between dark volcanic rocks"></div>
  <div class="hero-shadow"></div>

  <h2 class="tagline"><span class="big">Our Social Enterprise</span><span class="small">Established July 2001</span></h2>

  <footer class="footer">
    <div class="col" style="left:203px">
      <svg viewBox="0 0 28 38" width="28" style="margin-left:42px"><path d="M14 0C6.3 0 0 6.1 0 13.6 0 23.5 14 38 14 38s14-14.5 14-24.4C28 6.1 21.7 0 14 0z" fill="var(--orange)"/><circle cx="14" cy="13" r="4.5" fill="#fff"/></svg>
      <h3>Location &amp; Contacts</h3>
      <p>Harbour Lane, Kingston Bay<br>PO Box 914<br>Kingston Tide NSW 2999<br>SOUTH PACIFIC<br>N.B.N. 417 226 058</p>
    </div>
    <div class="divider" style="left:385px"></div>
    <div class="col" style="left:421px">
      <svg viewBox="0 0 38 38" width="38" style="margin-left:25px"><path d="M6 22c-2 4-1 8 2 11l2 2 6-7-3-4c2-6 7-11 13-13l4 3 7-6-2-2c-3-3-7-4-11-2C16 6 9 13 6 22z" fill="var(--orange)" transform="rotate(-10 19 19)"/></svg>
      <h3>Telephone</h3>
      <p class="tight">International + 64 9 555 0182<br>Australia 1800 555 314<br>New Zealand</p>
    </div>
    <div class="divider" style="left:583px"></div>
    <div class="col" style="left:607px">
      <svg viewBox="0 0 38 38" width="38" style="margin-left:62px"><circle cx="19" cy="19" r="16" fill="none" stroke="var(--orange)" stroke-width="5"/><circle cx="19" cy="19" r="6" fill="none" stroke="var(--orange)" stroke-width="4.5"/><path d="M25 13v9c0 4 6 4 6-2" fill="none" stroke="var(--orange)" stroke-width="4.5"/></svg>
      <h3>Email Website &amp; FriendBoard</h3>
      <p class="tight">hello@bluewatergetaways.org<br>www.bluewatergetaways.org<br>www.friendboard.net/<br>bluewatergetaways</p>
    </div>
    <div class="divider" style="left:800px"></div>
    <div class="col" style="left:823px">
      <svg viewBox="0 0 38 38" width="38" style="margin-left:33px"><rect x="1" y="15" width="36" height="21" rx="2" fill="var(--orange)"/><path d="M1 5l34-3 1 9-35 3z" fill="var(--orange)"/><path d="M8 4l5 9M17 3l5 9M26 2l5 9" stroke="#fff" stroke-width="2"/><path d="M1 21h36" stroke="#fff" stroke-width="1.5"/><rect x="17" y="25" width="2" height="5" fill="#fff"/></svg>
      <h3>Images &amp; Video</h3>
      <p class="tight">BLUEWATER VIDEO<br>to see more photographs and video's<br>LIKE our FRIENDBOARD page</p>
    </div>
    <div class="rule-bottom"></div>
    <div class="copy">© 2013 bluewatergetaways.org. All rights reserved.</div>
  </footer>
</div>
</body>
</html>
```